Book Cover for: TITLE Mend the Quiet Tide SUBTITLE For couples who don't want to break up

We need a full cover design for a book on relationships written by husband and wife team, Marla and Dennis Holtwick, PhD. This book will offer hope for couples that are on the verge of breaking up but want to work things out and stay together. The theme is to teach couples about their own reactions to their partner, how moods affect a relationship, how to get creative to solving problems and how to have a good feeling towards your partner regardless of differences. This book is about hope. It is a positive look at relationships that feel hopeless.

Target Market(s)

Married or couples that are going through a difficult time and are considering splitting up due to, communication difficulties, addiction, affair. We imagine the book will appeal to women more than men but still want a cover that men would be comfortable picking up.

Colors

Designer to choose colors to be used in the design.

Requirements
Must have
• We want the cover to beautiful, intriguing, simple and uncomplicated. We don't want it overly busy, technical, or complex.
Nice to have
• MAYBE?? a broken heart being put back together.
Should not have
• No photo, no cartoon, no flowers, no couple (unless obscure and not gender specific).

```html
<!DOCTYPE html>
<html lang="en">
<head>
<meta charset="utf-8">
<title>Mend the Quiet Tide — Book Cover</title>
<link rel="stylesheet" href="https://fonts.googleapis.com/css2?family=Bebas+Neue&family=Montserrat:wght@600;700&display=swap">
<style>
  :root {
    --page-bg: #e4e4e4;
    --cover-white: #ffffff;
    --title-red: #d20000;
    --ink: #111111;
    --subtitle-ink: #222222;
    --art-red: #e21d1d;
    --art-deep: #b81212;
    --band-dark: #120000;
    --band-red: #cc0000;
    --band-text: #ffffff;
  }
  * { margin: 0; padding: 0; box-sizing: border-box; }
  html, body {
    width: 1200px;
    height: 1200px;
    overflow: hidden;
    background: var(--page-bg);
  }
  .canvas {
    position: relative;
    width: 1200px;
    height: 1200px;
  }
  .book-cover {
    position: absolute;
    left: 248px;
    top: 55px;
    width: 705px;
    height: 1090px;
    background: var(--cover-white);
    overflow: hidden;
  }
  .cover-type {
    position: absolute;
    left: 0;
    top: 0;
    width: 705px;
    height: 620px;
  }
  .subtitle-text {
    font-family: "Montserrat", sans-serif;
    font-weight: 700;
    font-size: 31px;
    fill: var(--subtitle-ink);
  }
  .title-main {
    font-family: "Bebas Neue", "Oswald", sans-serif;
    fill: var(--title-red);
  }
  .title-middle {
    font-family: "Bebas Neue", "Oswald", sans-serif;
    fill: var(--ink);
  }
  .illustration-area {
    position: absolute;
    left: 153px;
    top: 635px;
    width: 380px;
    height: 350px;
    border-radius: 24px;
    background:
      radial-gradient(ellipse 60% 60% at 50% 45%, var(--art-red) 0%, var(--art-deep) 70%, rgba(184, 18, 18, 0.85) 100%);
  }
  .author-band {
    position: absolute;
    left: 0;
    bottom: 0;
    width: 705px;
    height: 76px;
    background: linear-gradient(90deg, var(--band-dark) 0%, #6e0000 30%, var(--band-red) 50%, #6e0000 70%, var(--band-dark) 100%);
    display: flex;
    align-items: center;
    justify-content: center;
  }
  .author-name {
    font-family: "Montserrat", sans-serif;
    font-weight: 700;
    font-size: 27px;
    letter-spacing: 0.5px;
    color: var(--band-text);
    white-space: nowrap;
  }
</style>
</head>
<body>
<div class="canvas">
  <article class="book-cover">
    <svg class="cover-type" viewBox="0 0 705 620" xmlns="http://www.w3.org/2000/svg">
      <defs>
        <linearGradient id="rule-fade" x1="0" x2="1" y1="0" y2="0">
          <stop offset="0" stop-color="#d20000" stop-opacity="0"/>
          <stop offset="0.5" stop-color="#d20000" stop-opacity="1"/>
          <stop offset="1" stop-color="#d20000" stop-opacity="0"/>
        </linearGradient>
      </defs>
      <g class="subtitle">
        <rect class="subtitle-rule" x="60" y="30" width="585" height="1" fill="url(#rule-fade)"/>
        <text class="subtitle-text" x="352.5" y="65" text-anchor="middle" textLength="327" lengthAdjust="spacingAndGlyphs">FOR COUPLES WHO</text>
        <text class="subtitle-text" x="352.5" y="98" text-anchor="middle" textLength="442" lengthAdjust="spacingAndGlyphs">DON'T WANT TO BREAK UP</text>
        <rect class="subtitle-rule" x="60" y="109" width="585" height="1" fill="url(#rule-fade)"/>
      </g>
      <g class="title">
        <text class="title-main" x="50" y="285" font-size="207" textLength="604" lengthAdjust="spacingAndGlyphs">MEND THE</text>
        <line class="title-rule" x1="50" y1="334" x2="226" y2="334" stroke="var(--ink)" stroke-width="2"/>
        <text class="title-middle" x="352.5" y="372" font-size="104" text-anchor="middle">QUIET</text>
        <line class="title-rule" x1="479" y1="334" x2="654" y2="334" stroke="var(--ink)" stroke-width="2"/>
        <text class="title-main" x="50" y="604" font-size="304" textLength="604" lengthAdjust="spacingAndGlyphs">TIDE</text>
      </g>
    </svg>
    <div class="illustration-area" role="img" aria-label="Illustration area: a cracked red heart mended with stitches and a bandage, wrapped in a strand of thorny wire"></div>
    <footer class="author-band">
      <p class="author-name">MARLA &amp; DENNIS HOLTWICK, PHD.</p>
    </footer>
  </article>
</div>
</body>
</html>
```